main page images

We are looking for three splash images to promote our services and technology in the accommodation, hospital and aged care facilities. The look and feel would be preferred to look like the image below, but with the mentioned screens and products for each.

```html
<!DOCTYPE html>
<html lang="en">
<head>
<meta charset="utf-8">
<title>Bedside Patient Terminal – Services</title>
<link rel="stylesheet" href="https://fonts.googleapis.com/css2?family=Roboto:wght@300;400;500&display=swap">
<style>
  :root {
    --backdrop: #9db3c6;
    --backdrop-deep: #7f97ad;
    --screen-top: #8a8f7a;
    --screen-mid: #4e5436;
    --screen-low: #2c2f22;
    --panel: rgba(40, 44, 40, 0.62);
    --panel-line: rgba(255, 255, 255, 0.35);
    --text: #ffffff;
    --text-dark: #16191c;
    --tile: rgba(255, 255, 255, 0.22);
    --tile-edge: rgba(255, 255, 255, 0.75);
    --icon: #ffffff;
  }
  * { margin: 0; padding: 0; box-sizing: border-box; }
  html, body { width: 1200px; height: 701px; overflow: hidden; }
  body { font-family: "Roboto", Arial, sans-serif; background: var(--backdrop); }
  .stage {
    position: relative; width: 1200px; height: 701px; overflow: hidden;
    background: linear-gradient(160deg, var(--backdrop) 0%, var(--backdrop-deep) 100%);
  }

  /* Terminal screen */
  .screen {
    position: absolute; left: 280px; top: 112px; width: 730px; height: 490px;
    color: var(--text);
  }
  .screen-scenery {
    position: absolute; inset: 0;
    background: linear-gradient(180deg, var(--screen-top) 0%, #6f6f4a 35%, var(--screen-mid) 60%, var(--screen-low) 100%);
  }
  .brand {
    position: absolute; top: 6px; left: 0; width: 100%; text-align: center;
    font-size: 12px; font-weight: 500; letter-spacing: 0.5px;
  }
  .customer-logo {
    position: absolute; left: 30px; top: 25px; width: 142px; height: 40px;
    border: 2px solid var(--text); border-radius: 4px;
    font-size: 16px; line-height: 36px; text-align: center; font-weight: 400;
  }
  .clock {
    position: absolute; top: 18px; left: 0; width: 100%; text-align: center;
    color: var(--text-dark);
  }
  .clock-time { font-size: 44px; font-weight: 400; line-height: 1; }
  .clock-date { font-size: 14px; margin-top: 6px; }

  .panel { position: absolute; background: var(--panel); border-radius: 4px; }

  .care-team { left: 35px; top: 115px; width: 250px; height: 370px; padding: 12px 14px; }
  .room-line {
    font-size: 15px; padding-bottom: 6px; border-bottom: 1px solid var(--panel-line);
    display: flex; gap: 12px;
  }
  .role { font-size: 14px; letter-spacing: 0.4px; margin-top: 12px; }
  .member { display: flex; gap: 10px; margin-top: 6px; align-items: center; }
  .portrait { width: 48px; height: 58px; background: linear-gradient(180deg, #6b5a4c, #3a2f27); flex: none; }
  .member-name { font-size: 14px; }
  .member-phone { font-size: 14px; margin-top: 2px; }

  .media { left: 300px; top: 100px; width: 210px; height: 78px; display: flex; gap: 8px; padding: 10px 12px; }
  .media-tile { flex: 1; border-radius: 2px; }
  .media-tile.news { background: #2b5fb0; }
  .media-tile.film-a { background: #5b3b2a; }
  .media-tile.film-b { background: #8a8478; }
  .media-tile.radio { background: #c8373b; }

  .pain { left: 300px; top: 190px; width: 210px; height: 95px; padding: 14px 12px; font-size: 13px; }
  .pain-row { display: flex; align-items: center; gap: 10px; margin-bottom: 14px; }
  .pain-row svg { flex: none; }

  .tasks { left: 300px; top: 300px; width: 210px; height: 95px; padding: 10px 12px; font-size: 12px; }
  .task { display: flex; align-items: center; gap: 10px; }
  .task + .task { margin-top: 4px; }
  .box { width: 20px; height: 20px; border: 1.5px solid var(--text); flex: none; }

  .vitals { left: 525px; top: 95px; width: 185px; height: 260px; padding: 14px 12px; font-size: 12px; }
  .vital { display: flex; align-items: center; gap: 10px; height: 42px; }
  .vital-icon { width: 22px; height: 22px; border-radius: 4px; background: rgba(255,255,255,0.85); flex: none; }

  /* Floating service tiles */
  .service-tile {
    position: absolute; background: var(--tile); border: 1px solid var(--tile-edge);
    display: flex; align-items: center; justify-content: center;
  }
  .service-tile svg { fill: none; stroke: var(--icon); stroke-width: 4; stroke-linecap: round; stroke-linejoin: round; }
  .network-name { font-size: 26px; font-weight: 500; color: var(--icon); }
</style>
</head>
<body>
<main class="stage">

  <section class="screen">
    <div class="screen-scenery" role="img" aria-label="Mountain valley landscape with river at dusk"></div>
    <div class="brand">SOLVERA</div>
    <div class="customer-logo">Customer Logo</div>
    <div class="clock">
      <div class="clock-time">1:43 AM</div>
      <div class="clock-date">Wednesday, July 12, 2017</div>
    </div>

    <div class="panel care-team">
      <div class="room-line"><span>Room 17</span><span>Bed 1</span><span>555-014-2270</span></div>
      <div class="role">PRIMARY CARE PHYSICIAN</div>
      <div class="member">
        <div class="portrait" role="img" aria-label="Physician portrait"></div>
        <div><div class="member-name">Lena Ortiz, MD</div><div class="member-phone">555.010.4432</div></div>
      </div>
      <div class="role">CONSULTANT</div>
      <div class="member">
        <div class="portrait" role="img" aria-label="Consultant portrait"></div>
        <div><div class="member-name">Owen Carter</div><div class="member-phone">555.010.4432</div></div>
      </div>
      <div class="role">NURSE</div>
      <div class="member">
        <div class="portrait" role="img" aria-label="Nurse portrait"></div>
        <div><div class="member-name">Paul Hendry</div><div class="member-phone">555.010.4432</div></div>
      </div>
    </div>

    <div class="panel media">
      <div class="media-tile news" role="img" aria-label="News channel"></div>
      <div class="media-tile film-a" role="img" aria-label="Film poster"></div>
      <div class="media-tile film-b" role="img" aria-label="Music album"></div>
      <div class="media-tile radio" role="img" aria-label="Radio station"></div>
    </div>

    <div class="panel pain">
      <div class="pain-row">
        <svg width="22" height="16" viewBox="0 0 22 16"><rect x="1" y="4" width="20" height="8" rx="4" fill="none" stroke="#fff" stroke-width="1.5"/><line x1="11" y1="4" x2="11" y2="12" stroke="#fff" stroke-width="1.5"/></svg>
        <span>Current Pain: Unknown</span>
      </div>
      <div class="pain-row">
        <svg width="22" height="22" viewBox="0 0 22 22"><circle cx="11" cy="11" r="9" fill="none" stroke="#fff" stroke-width="1.5"/><circle cx="8" cy="9" r="1" fill="#fff"/><circle cx="14" cy="9" r="1" fill="#fff"/><path d="M7 14 Q11 17 15 14" fill="none" stroke="#fff" stroke-width="1.5"/></svg>
        <span>Current Pain Goal: 4</span>
      </div>
    </div>

    <div class="panel tasks">
      <div class="task">
        <svg width="20" height="20" viewBox="0 0 20 20"><rect x="1" y="1" width="18" height="18" fill="none" stroke="#fff" stroke-width="1.5"/><path d="M4 10 L8 14 L16 5" fill="none" stroke="#fff" stroke-width="2"/></svg>
        <span>Use your incentive spirometer every hour</span>
      </div>
      <div class="task"><span class="box"></span><span>Learn about your diet restrictions</span></div>
    </div>

    <div class="panel vitals">
      <div class="vital"><span class="vital-icon"></span><span>160.0 lbs</span></div>
      <div class="vital"><span class="vital-icon"></span><span>97.8° F</span></div>
      <div class="vital"><span class="vital-icon"></span><span>92 beats per minute</span></div>
      <div class="vital"><span class="vital-icon"></span><span>26 breaths per minute</span></div>
      <div class="vital"><span class="vital-icon"></span><span>98% oxygen</span></div>
    </div>
  </section>

  <!-- Service tiles -->
  <div class="service-tile" style="left:1049px;top:80px;width:107px;height:107px" aria-label="Bedside terminal">
    <svg width="60" height="80" viewBox="0 0 60 80"><rect x="8" y="4" width="44" height="56" rx="3"/><rect x="18" y="12" width="24" height="22"/><rect x="20" y="40" width="20" height="8" rx="4"/><line x1="30" y1="60" x2="30" y2="70"/><line x1="12" y1="74" x2="48" y2="74"/></svg>
  </div>
  <div class="service-tile" style="left:838px;top:138px;width:67px;height:67px"></div>
  <div class="service-tile" style="left:175px;top:180px;width:106px;height:106px" aria-label="Patient survey">
    <svg width="64" height="84" viewBox="0 0 64 84"><rect x="4" y="10" width="56" height="70" rx="5"/><rect x="20" y="4" width="24" height="12" rx="3"/><rect x="12" y="28" width="10" height="10"/><path d="M13 33 L17 37 L24 27"/><rect x="12" y="46" width="10" height="10"/><rect x="12" y="64" width="10" height="10"/><line x1="30" y1="33" x2="52" y2="33"/><line x1="30" y1="51" x2="46" y2="51"/><line x1="30" y1="69" x2="38" y2="69"/></svg>
  </div>
  <div class="service-tile" style="left:339px;top:232px;width:77px;height:68px" aria-label="Meal ordering">
    <svg width="46" height="56" viewBox="0 0 46 56"><rect x="4" y="4" width="38" height="48" rx="4"/><path d="M12 24 Q23 10 34 24 Z"/><line x1="12" y1="30" x2="34" y2="30"/><rect x="12" y="34" width="22" height="6" rx="3"/></svg>
  </div>
  <div class="service-tile" style="left:12px;top:289px;width:94px;height:94px" aria-label="Nurse call">
    <svg width="64" height="64" viewBox="0 0 64 64"><path d="M10 50 Q10 28 32 28 Q54 28 54 50 Z"/><line x1="32" y1="22" x2="32" y2="28"/><line x1="6" y1="56" x2="58" y2="56"/><rect x="6" y="4" width="8" height="16"/><path d="M14 8 H40 Q48 8 50 16"/></svg>
  </div>
  <div class="service-tile" style="left:107px;top:371px;width:70px;height:70px" aria-label="Translation">
    <svg width="50" height="50" viewBox="0 0 50 50"><rect x="4" y="18" width="24" height="20" rx="3"/><path d="M10 38 L10 46 L16 38"/><rect x="22" y="4" width="24" height="20" rx="3"/><path d="M11 33 L16 22 L21 33 M13 29 H19"/><path d="M28 10 H40 M34 8 V12 M30 18 Q36 16 38 10"/></svg>
  </div>
  <div class="service-tile" style="left:218px;top:346px;width:136px;height:136px" aria-label="Multi-device access">
    <svg width="110" height="110" viewBox="0 0 110 110"><rect x="20" y="8" width="66" height="78" rx="5"/><rect x="6" y="62" width="28" height="44" rx="4"/><rect x="72" y="56" width="32" height="50" rx="4"/><line x1="32" y1="60" x2="70" y2="22"/><line x1="12" y1="94" x2="28" y2="76"/><line x1="80" y1="90" x2="98" y2="68"/></svg>
  </div>
  <div class="service-tile" style="left:581px;top:262px;width:67px;height:67px" aria-label="Touch screen">
    <svg width="50" height="50" viewBox="0 0 50 50"><rect x="4" y="6" width="40" height="28" rx="3"/><path d="M26 46 V24 Q26 20 29 20 Q32 20 32 24 V32 L40 34 V46"/></svg>
  </div>
  <div class="service-tile" style="left:741px;top:237px;width:117px;height:117px" aria-label="Wireless network">
    <span class="network-name">AirNet</span>
  </div>
  <div class="service-tile" style="left:925px;top:235px;width:97px;height:97px" aria-label="Information kiosk">
    <svg width="76" height="76" viewBox="0 0 76 76"><path d="M6 6 H34 L44 30 V68 H6 Z"/><rect x="44" y="40" width="28" height="28" rx="14"/><line x1="58" y1="50" x2="56" y2="62"/><circle cx="59" cy="45" r="1" fill="#fff"/></svg>
  </div>
  <div class="service-tile" style="left:768px;top:377px;width:141px;height:141px" aria-label="Location services">
    <svg width="90" height="120" viewBox="0 0 90 120"><path d="M15 22 Q45 -2 75 22"/><path d="M25 32 Q45 16 65 32"/><path d="M45 44 Q26 44 26 64 Q26 80 45 110 Q64 80 64 64 Q64 44 45 44 Z"/><circle cx="45" cy="64" r="7"/></svg>
  </div>

</main>
</body>
</html>
```